New National Dermatology Group needs a business card!

We need a business card for our new national company that has 3 brands within the business:
Brindlewood Clinics Australia, Harrowmere Clinics Australia and Tallowfen Clinics Australia.
We help people access dermatology services close to home throughout Australia.
We need a business card that has:
all 3 logos on it,
Our websites (there are three, listed above)
Our email (there are three, listed above)
The location of our first clinic: 41 Wren St Parramatta (this can then be changed for each location as required)

```html
<!DOCTYPE html>
<html lang="en">
<head>
<meta charset="utf-8">
<title>Business Card</title>
<link href="https://fonts.googleapis.com/css2?family=Cinzel:wght@600&family=Open+Sans:wght@400&display=swap" rel="stylesheet">
<style>
  :root {
    --brown: #7a3c1b;
    --orange: #f2842c;
    --green: #21ad4b;
    --white: #ffffff;
    --backdrop: #2e2e2e;
  }
  html, body {
    margin: 0;
    width: 1200px;
    height: 866px;
    overflow: hidden;
    background: var(--backdrop);
  }
  .card {
    position: absolute;
    left: 100px;
    top: 147px;
    width: 1000px;
    height: 571px;
    color: var(--white);
  }
  .card-shapes {
    position: absolute;
    inset: 0;
    width: 100%;
    height: 100%;
  }
  .brand {
    position: absolute;
  }
  .brand-name {
    font-family: "Cinzel", serif;
    font-weight: 600;
    margin: 0;
    line-height: 1;
    letter-spacing: 1px;
  }
  .brand-name .line-main {
    display: block;
  }
  .brand-name .line-sub {
    display: block;
    font-size: 0.42em;
    letter-spacing: 5px;
    margin-top: 6px;
  }
  .contact {
    font-family: "Open Sans", sans-serif;
    font-size: 19px;
    line-height: 1.3;
    margin-top: 14px;
  }
  .contact-row {
    display: flex;
    align-items: center;
    gap: 10px;
  }
  .contact-row svg {
    width: 20px;
    height: 20px;
    flex: none;
  }
  .brand--brindlewood { left: 36px; top: 170px; }
  .brand--brindlewood .brand-name { font-size: 36px; }
  .brand--tallowfen { left: 480px; top: 60px; }
  .brand--tallowfen .brand-name { font-size: 48px; }
  .brand--harrowmere { right: 48px; top: 368px; text-align: right; }
  .brand--harrowmere .brand-name { font-size: 42px; }
  .brand--harrowmere .contact-row { justify-content: flex-end; }
</style>
</head>
<body>
<div class="card">
  <svg class="card-shapes" viewBox="0 0 1000 571" preserveAspectRatio="none" aria-hidden="true">
    <rect width="1000" height="571" fill="var(--orange)"/>
    <polygon points="0,0 330,0 448,300 296,571 0,571" fill="var(--brown)"/>
    <polygon points="482,336 1000,286 1000,571 330,571" fill="var(--green)"/>
    <g stroke="var(--white)" stroke-width="7" fill="none">
      <polyline points="338,0 456,300 304,571"/>
      <polyline points="1000,280 476,330 322,571"/>
    </g>
  </svg>

  <div class="brand brand--brindlewood">
    <h2 class="brand-name"><span class="line-main">BRINDLEWOOD</span><span class="line-sub">CLINICS AUSTRALIA</span></h2>
    <div class="contact">
      <div class="contact-row">
        <svg viewBox="0 0 20 20"><rect x="1" y="4" width="18" height="12" fill="var(--white)"/><polyline points="1,4 10,11 19,4" fill="none" stroke="var(--brown)" stroke-width="1.5"/></svg>
        <span>info@brindlewood.com.au</span>
      </div>
      <div class="contact-row">
        <svg viewBox="0 0 20 20"><g fill="none" stroke="var(--white)" stroke-width="1.6"><circle cx="10" cy="10" r="8"/><ellipse cx="10" cy="10" rx="3.5" ry="8"/><line x1="2" y1="10" x2="18" y2="10"/></g></svg>
        <span>www.brindlewood.com.au</span>
      </div>
      <div>41 Wren St Parramatta</div>
    </div>
  </div>

  <div class="brand brand--tallowfen">
    <h2 class="brand-name"><span class="line-main">TALLOWFEN</span><span class="line-sub">CLINICS AUSTRALIA</span></h2>
    <div class="contact">
      <div class="contact-row">
        <svg viewBox="0 0 20 20"><rect x="1" y="4" width="18" height="12" fill="var(--white)"/><polyline points="1,4 10,11 19,4" fill="none" stroke="var(--orange)" stroke-width="1.5"/></svg>
        <span>info@tallowfen.com.au</span>
      </div>
      <div class="contact-row">
        <svg viewBox="0 0 20 20"><g fill="none" stroke="var(--white)" stroke-width="1.6"><circle cx="10" cy="10" r="8"/><ellipse cx="10" cy="10" rx="3.5" ry="8"/><line x1="2" y1="10" x2="18" y2="10"/></g></svg>
        <span>www.tallowfen.com.au</span>
      </div>
      <div>41 Wren St Parramatta</div>
    </div>
  </div>

  <div class="brand brand--harrowmere">
    <h2 class="brand-name"><span class="line-main">HARROWMERE</span><span class="line-sub">CLINICS AUSTRALIA</span></h2>
    <div class="contact">
      <div class="contact-row">
        <span>info@harrowmere.com.au</span>
        <svg viewBox="0 0 20 20"><rect x="1" y="4" width="18" height="12" fill="var(--white)"/><polyline points="1,4 10,11 19,4" fill="none" stroke="var(--green)" stroke-width="1.5"/></svg>
      </div>
      <div class="contact-row">
        <span>www.harrowmere.com.au</span>
        <svg viewBox="0 0 20 20"><g fill="none" stroke="var(--white)" stroke-width="1.6"><circle cx="10" cy="10" r="8"/><ellipse cx="10" cy="10" rx="3.5" ry="8"/><line x1="2" y1="10" x2="18" y2="10"/></g></svg>
      </div>
      <div>41 Wren St Parramatta</div>
    </div>
  </div>
</div>
</body>
</html>
```